Home Page Redesign for Pet Website

Looking to redesign the home page of our WORDPRESS website which will be renamed The Critter Cover Handbook 2015.

Looking for clean design which communicates clarity.
Updates

This is for a Wordpress site.

Please note that the design MUST include the content which is shown in the table in the brief!

Hi Thanks for the designs so far. We have just updated the brief to provide more information and clarify a few issues. We have also now included a couple of layout suggestions. They are just suggestions but it should give you a better idea of what we are looking for. And we have just increased the budget for 1st place by £120. Please feel free to message me if you have any questions. Many thanks. Maud

Please note that the new brief is in a file dated 25 Jan!

Reason: We have extended the deadline so we can continue working with the designers who have submitted designs we like. If you have any new designs please submit them by the original deadline of 7.37pm this evening (GMT). We are planning to make our final decision by Friday this week.

Target Market(s)

UK pet owners. All ages but largest age group is 35-50.

Industry/Entity Type

Insurance

Requirements
Must have
• Three clear content groups - LEARN, RESEARCH, CAMPAIGN (see brief for more details).
Stock photos with dogs and cats
Use current colour scheme
Must work with existing inner pages.
Existing font.. but 1pt larger
See brief for more details
Should not have
• Logo
Content from Existing Page (except for footer content... and menu headings).

```html
<!DOCTYPE html>
<html lang="en">
<head>
<meta charset="utf-8">
<title>The Critter Cover Handbook 2015</title>
<link rel="stylesheet" href="https://fonts.googleapis.com/css2?family=Archivo+Narrow:wght@400;700&family=Noto+Serif:wght@700&family=Source+Sans+Pro:wght@400;600;700&display=swap">
<style>
:root{
  --orange:#f26f21;
  --orange-light:#f8951d;
  --blue:#2d7fd8;
  --green:#3ab54a;
  --ink:#1f1f1f;
  --text:#3c3c3c;
  --muted:#777;
  --paper:#f1ede7;
  --band:#e2d9cc;
  --white:#ffffff;
  --rule:#d8d2c8;
  --fb:#3b5b9a;
  --tw:#4aa3d9;
}
*{box-sizing:border-box;margin:0;padding:0}
html,body{width:1200px;height:2404px;overflow:hidden}
body{font-family:"Source Sans Pro",Arial,sans-serif;color:var(--text);background:var(--paper)}
.page{position:relative;width:1200px;height:2404px;overflow:hidden;background:var(--paper)}
.abs{position:absolute}
ul{list-style:none}

/* top bar */
.topbar{left:0;top:0;width:1200px;height:46px;background:var(--orange)}
.topbar .social{position:absolute;left:160px;top:12px;display:flex;gap:8px}
.topbar .social span{width:20px;height:20px;border-radius:50%;background:var(--white)}
.search{position:absolute;left:834px;top:8px;width:204px;height:30px;background:var(--white);border-radius:2px;font-size:12px;color:#666;padding:8px 10px;line-height:14px}
.search svg{position:absolute;right:8px;top:6px}

/* header */
.header{left:0;top:46px;width:1200px;height:84px;background:var(--white)}
.brand{position:absolute;left:160px;top:20px;font-family:"Noto Serif",Georgia,serif;font-weight:700;font-size:19px;line-height:21px;color:var(--ink);width:230px}
.nav{position:absolute;left:442px;top:35px;width:596px;display:flex;justify-content:space-between;font-size:12px;font-weight:700;color:var(--ink);text-transform:uppercase;white-space:nowrap}
.nav .drop::after{content:"";display:inline-block;margin-left:4px;border:4px solid transparent;border-top:5px solid var(--orange);vertical-align:-2px}

/* hero */
.hero{left:0;top:130px;width:1200px;height:380px;background:linear-gradient(180deg,#c9dced 0%,#e6eef4 45%,#b7c98e 82%,#6f9a3c 100%)}
.hero-title{position:absolute;left:0;top:282px;width:1200px;text-align:center;font-family:"Archivo Narrow",Arial,sans-serif;font-weight:700;font-size:38px;line-height:44px;color:var(--white);letter-spacing:.5px}
.hero-sub{position:absolute;left:0;top:330px;width:1200px;text-align:center;font-size:14px;font-weight:600;color:#1c1c1c}

/* three groups */
.group{top:506px;width:280px}
.group .bar{height:3px}
.group h2{font-family:"Archivo Narrow",Arial,sans-serif;font-weight:700;font-size:30px;line-height:30px;margin-top:18px}
.group .lead{font-size:14px;color:var(--text);margin-top:2px}
.learn{left:160px}.learn .bar{background:var(--blue)}.learn h2{color:var(--blue)}
.research{left:460px}.research .bar{background:var(--orange)}.research h2{color:var(--orange)}
.campaign{left:760px}.campaign .bar{background:var(--green)}.campaign h2{color:var(--green)}
.links{margin-top:22px}
.links li{font-size:11px;color:var(--ink);padding:0 0 0 14px;height:39px;line-height:18px;position:relative;border-bottom:1px solid var(--rule);white-space:nowrap}
.links li::before{content:"";position:absolute;left:1px;top:6px;width:5px;height:5px;border-right:1.5px solid var(--blue);border-bottom:1.5px solid var(--blue);transform:rotate(-45deg)}
.research .links li::before{border-color:var(--orange)}
.campaign .links li::before{border-color:var(--green)}
.links li.tall{height:auto;padding-bottom:10px;margin-bottom:10px;white-space:normal}
.links li.bold{font-weight:700}
.providers{display:grid;grid-template-columns:1fr 1fr;column-gap:10px;margin:0 0 6px 0;border-bottom:1px solid var(--rule);padding-bottom:10px}
.providers li{font-size:11px;color:var(--ink);height:39px;padding-left:16px;position:relative;border-bottom:1px solid var(--rule);line-height:18px;white-space:nowrap}
.providers li::before{content:"";position:absolute;left:4px;top:7px;width:4px;height:4px;border-radius:50%;background:var(--orange)}
.providers li:nth-last-child(-n+2){border-bottom:0}

/* bands */
.band{left:0;width:1200px;background:var(--band)}
.band svg.edge{position:absolute;left:0;width:1200px;height:12px}
.help{top:1085px;height:204px}
.help h3{position:absolute;left:0;top:44px;width:1200px;text-align:center;font-family:"Archivo Narrow",Arial,sans-serif;font-weight:700;font-size:31px;line-height:36px;color:var(--ink)}
.help p{position:absolute;left:0;top:84px;width:1200px;text-align:center;font-size:13px;color:var(--ink)}
.btn{position:absolute;left:533px;top:118px;width:130px;height:36px;border-radius:3px;background:linear-gradient(180deg,var(--orange-light),var(--orange));color:var(--white);font-size:13px;font-weight:600;text-align:center;line-height:36px}

/* content row */
.content{left:0;top:1289px;width:1200px;height:411px;background:var(--white)}
.col{position:absolute;top:36px;width:280px}
.col h2{font-family:"Archivo Narrow",Arial,sans-serif;font-weight:700;font-size:31px;color:var(--blue);line-height:34px}
.article{margin-top:22px;border-bottom:1px solid var(--rule);padding-bottom:12px}
.article h4{font-size:14px;font-weight:700;color:var(--ink)}
.article p{font-size:12px;line-height:18px;color:var(--muted);margin-top:6px}
.stars{display:flex;gap:3px;margin-top:10px}
.stars span{width:10px;height:10px;background:#444;clip-path:polygon(50% 0,62% 36%,100% 38%,70% 60%,80% 100%,50% 76%,20% 100%,30% 60%,0 38%,38% 36%)}
.stars span.on{background:#f2b51a}
.more{display:inline-block;margin-top:12px;font-size:10px;background:#e4e2df;color:#333;padding:4px 7px;border-radius:2px}
.res{margin-top:20px}
.res li{font-size:13px;color:var(--ink);height:39px;line-height:20px;padding-left:14px;position:relative;border-bottom:1px solid var(--rule);white-space:nowrap}
.res li::before{content:"";position:absolute;left:1px;top:7px;width:5px;height:5px;border-right:1.5px solid var(--blue);border-bottom:1.5px solid var(--blue);transform:rotate(-45deg)}
.disc p{font-size:11.5px;line-height:18px;color:var(--muted);margin-top:20px}

/* newsletter */
.news{top:1700px;height:170px}
.news h3{position:absolute;left:0;top:38px;width:1200px;text-align:center;font-family:"Archivo Narrow",Arial,sans-serif;font-weight:700;font-size:25px;line-height:30px;color:var(--ink)}
.news p{position:absolute;left:0;top:70px;width:1200px;text-align:center;font-size:12px;color:var(--ink)}
.field{position:absolute;left:316px;top:92px;width:370px;height:36px;background:var(--white);border:1px solid #d4cec4;font-size:12px;color:#555;padding:10px 14px;line-height:14px}
.subscribe{position:absolute;left:686px;top:92px;width:196px;height:36px;background:linear-gradient(180deg,var(--orange-light),var(--orange));color:var(--white);font-size:13px;font-weight:600;text-align:center;line-height:36px}

/* widgets */
.widgets{left:0;top:1870px;width:1200px;height:310px;background:#f4f2ef}
.widget{position:absolute;top:42px;width:278px;height:226px;background:var(--white);border:1px solid #ccc;overflow:hidden}
.widget .head{height:34px;color:var(--white);font-size:14px;font-weight:700;line-height:34px;padding-left:14px;text-transform:uppercase;display:flex;align-items:center;gap:8px}
.widget .head i{width:14px;height:14px;background:var(--white);display:inline-block}
.fbw{left:160px}.fbw .head{background:var(--fb)}
.tww{left:486px}.tww .head{background:var(--tw)}
.avatar{width:32px;height:32px;background:#c8b4a2;display:inline-block;flex:none}
.fb-top{display:flex;gap:8px;padding:8px 10px;font-size:12px;color:var(--fb)}
.like{margin-top:4px;font-size:10px;color:#333}
.like b{background:var(--fb);color:var(--white);padding:1px 4px;border-radius:2px;margin-right:4px}
.fb-feed{margin:6px 10px;border:1px solid #ccc;height:118px;padding:8px;font-size:10px;line-height:13px;color:#222;display:flex;gap:8px;overflow:hidden}
.fb-feed .meta{color:var(--fb);font-size:11px}
.fb-feed small{color:#999;font-size:9px;display:block}
.tw-body{padding:6px 10px;font-size:10px;line-height:12px;color:#222}
.tw-body .row{display:flex;justify-content:space-between;border-bottom:1px solid #ddd;padding-bottom:4px;color:var(--tw);font-size:12px}
.follow{font-size:9px;border:1px solid #ccc;padding:1px 6px;color:#333;border-radius:2px}
.tweet{display:flex;gap:8px;padding:8px 0;border-bottom:1px solid #eee}
.tweet .avatar{width:24px;height:24px}
.tweet .name{font-weight:700}
.tweet .handle{color:#999}
.tweet .date{margin-left:auto;color:#999;flex:none}
.tweetbox{margin-top:6px;border:1px solid #ccc;padding:5px;color:#666}
.ad{position:absolute;left:812px;top:42px;width:226px;height:226px;background:var(--orange);color:var(--white);font-size:13px;text-align:center;padding-top:98px;line-height:16px}

/* footer */
.footer{left:0;top:2180px;width:1200px;height:224px;background:var(--paper)}
.counts{position:absolute;left:270px;top:50px;display:flex;gap:44px}
.count{display:flex;align-items:center}
.count .dot{width:40px;height:40px;border-radius:50%;position:relative;z-index:1}
.count .pill{margin-left:-4px;width:60px;height:20px;background:#d7d0c6;color:var(--white);font-size:9px;line-height:20px;text-align:center}
.foot-links{position:absolute;left:0;top:124px;width:1200px;text-align:center;font-size:12px;color:var(--ink)}
.foot-links span{margin:0 12px}
.copy{position:absolute;left:0;top:144px;width:1200px;text-align:center;font-size:12px;line-height:18px;color:var(--ink)}
</style>
</head>
<body>
<div class="page">

  <div class="abs topbar">
    <div class="social"><span></span><span></span><span></span><span></span><span></span></div>
    <div class="search">Search
      <svg width="16" height="16" viewBox="0 0 16 16"><circle cx="6.5" cy="6.5" r="5" fill="none" stroke="#bbb" stroke-width="2"/><line x1="10" y1="10" x2="15" y2="15" stroke="#bbb" stroke-width="2"/></svg>
    </div>
  </div>

  <header class="abs header">
    <div class="brand">The Critter Cover<br>Handbook 2015</div>
    <nav class="nav">
      <span>Home</span><span>Pet Insurance Reviews</span><span>Providers A-Z</span><span class="drop">Pet Insurance Policies</span><span>Surveys</span><span class="drop">More</span>
    </nav>
  </header>

  <section class="abs hero" role="img" aria-label="Photo of a cat and a puppy sitting together on green grass under a pale sky">
    <div class="hero-title">THE CRITTER COVER HANDBOOK 2015</div>
    <div class="hero-sub">Independent unbiased information for fellow pet owners</div>
  </section>

  <section class="abs group learn">
    <div class="bar"></div>
    <h2>LEARN</h2>
    <div class="lead">About Pet Insurance</div>
    <ul class="links">
      <li>Introduction to Pet Insurance</li>
      <li>Vet Fees Cover Types</li>
      <li>What to Consider before Buying</li>
      <li>Ten Popular Pet Insurance Providers</li>
      <li>Confused by Pet Insurance: Start Here!</li>
      <li>Third Party Liability Insurance</li>
      <li>Six Vet Fees Pet Insurance Companies Won't Pay!</li>
      <li>Why Cheap Pet Insurance is Risky</li>
      <li>Why Your Pets Vet History is Important</li>
    </ul>
  </section>

  <section class="abs group research">
    <div class="bar"></div>
    <h2>RESEARCH</h2>
    <div class="lead">UK Pet Insurance Policies</div>
    <ul class="links">
      <li class="tall bold">Analysis, Customer Reviews and Full Details of All UK Policies</li>
    </ul>
    <ul class="providers">
      <li>Critter Companions</li><li>Kennel Circle</li>
      <li>Argyle</li><li>N&amp;T</li>
      <li>Straight Path</li><li>Much More</li>
      <li>F&amp;M</li><li>Paw Plan</li>
      <li>Hearty Paws</li><li>Sandbury's</li>
      <li>Helpcoverly</li><li>Tessa Co</li>
      <li>James Lowell</li><li>Vermilion Money</li>
      <li>KW</li><li>Other Providers</li>
    </ul>
    <ul class="links" style="margin-top:4px">
      <li class="tall">Search our database for policies matching your criteria</li>
      <li class="tall" style="border-bottom:0">Compare claims experiences for pet insurance providers</li>
    </ul>
  </section>

  <section class="abs group campaign">
    <div class="bar"></div>
    <h2>CAMPAIGN</h2>
    <div class="lead">For Fairer Pet Insurance</div>
    <ul class="links">
      <li>This section will contain paragraphs of text</li>
      <li>Brief explanation of why a campaign is needed.</li>
      <li>Brief explanation of what to campaign for.</li>
      <li>Bio pic of me.... plus brief bio.</li>
      <li>How you can help</li>
      <li>Stories with Pet Pics.</li>
    </ul>
  </section>

  <section class="abs band help">
    <svg class="edge" style="top:-6px" viewBox="0 0 1200 12" preserveAspectRatio="none"><path d="M0 6 L60 3 L130 7 L220 2 L320 6 L420 3 L520 8 L620 3 L720 6 L830 2 L930 7 L1030 3 L1120 6 L1200 3 L1200 12 L0 12Z" fill="#e2d9cc"/></svg>
    <h3>NEED HELP FINDING THE RIGHT CRITTER COVER HANDBOOK 2015</h3>
    <p>We make it easy for you.</p>
    <div class="btn">Get Started</div>
    <svg class="edge" style="bottom:-6px" viewBox="0 0 1200 12" preserveAspectRatio="none"><path d="M0 0 L1200 0 L1200 6 L1100 9 L990 4 L880 8 L760 3 L650 9 L540 5 L430 9 L320 4 L210 8 L100 4 L0 7Z" fill="#e2d9cc"/></svg>
  </section>

  <section class="abs content">
    <div class="col" style="left:160px">
      <h2>POPULAR ARTICLES</h2>
      <div class="article">
        <h4>Lorem ipsum dolor sit amet</h4>
        <p>Sed do eiusmod tempor incididunt ut labore et dolore magna aliqua.</p>
        <div class="stars"><span class="on"></span><span class="on"></span><span></span><span></span><span></span></div>
        <span class="more">Read more</span>
      </div>
      <div class="article" style="border-bottom:0">
        <h4>Lorem ipsum dolor sit amet</h4>
        <p>Sed do eiusmod tempor incididunt ut labore et dolore magna aliqua.</p>
        <div class="stars"><span class="on"></span><span class="on"></span><span></span><span></span><span></span></div>
        <span class="more">Read more</span>
      </div>
    </div>
    <div class="col" style="left:460px">
      <h2>RESOURCES</h2>
      <ul class="res">
        <li>Lorem ipsum dolor sit amet</li>
        <li>Sed ut perspiciatis unde omnis</li>
        <li>Beatae vitae dicta sunt explicabo</li>
        <li>Nemo enim ipsam voluptatem</li>
        <li>Neque porro quisquam est</li>
        <li>Quis autem vel eum iure</li>
        <li style="border-bottom:0">At vero eos et accusamus et</li>
      </ul>
    </div>
    <div class="col disc" style="left:760px">
      <h2>DISCLAIMER</h2>
      <p>Please note that pet insurance terms often change. Whilst we will do our best to keep this website up to date you must check with the appropriate insurer before making any decisions. If you find any mistakes on this website please do let us know so we can correct it for the benefit of future visitors. Many thanks!</p>
      <p>Sed ut perspiciatis unde omnis iste natus error sit voluptatem accusantium doloremque laudantium, totam rem aperiam, eaque ipsa quae ab illo inventore veritatis et quasi architecto beatae vitae dicta sunt explicabo. Nemo enim ipsam voluptatem quia voluptas sit aspernatur aut odit aut fugit, sed quia consequuntur</p>
    </div>
  </section>

  <section class="abs band news">
    <svg class="edge" style="top:-6px" viewBox="0 0 1200 12" preserveAspectRatio="none"><path d="M0 7 L90 3 L180 8 L290 3 L400 7 L500 2 L610 7 L720 3 L820 8 L930 3 L1040 7 L1130 3 L1200 6 L1200 12 L0 12Z" fill="#e2d9cc"/></svg>
    <h3># THE CRITTER COVER HANDBOOK 2015</h3>
    <p>Enter your email address below to receive site offers,discounts, and promotions</p>
    <div class="field">Enter your email</div>
    <div class="subscribe">Subscribe To Our Newsletter</div>
    <svg class="edge" style="bottom:-6px" viewBox="0 0 1200 12" preserveAspectRatio="none"><path d="M0 0 L1200 0 L1200 7 L1090 3 L980 8 L870 4 L760 9 L650 4 L540 8 L430 3 L320 8 L210 4 L100 8 L0 5Z" fill="#e2d9cc"/></svg>
  </section>

  <section class="abs widgets">
    <div class="widget fbw">
      <div class="head"><i></i>Join us on Facepage</div>
      <div class="fb-top">
        <span class="avatar" role="img" aria-label="Profile picture"></span>
        <div>Critter Cover Handbook 2015<div class="like"><b>Like</b>1,176</div></div>
      </div>
      <div class="fb-feed">
        <span class="avatar" style="width:24px;height:24px" role="img" aria-label="Profile picture"></span>
        <div><div class="meta">Critter Cover Handbook 2015</div><small>January 18 at 11:43pm</small><b>Pet Insurance Premium Increases</b><br>Interesting article from Whichway? suggesting that pet insurance premiums can double as your pet</div>
      </div>
    </div>

    <div class="widget tww">
      <div class="head"><i></i>Latest from Chirper</div>
      <div class="tw-body">
        <div class="row"><span>Posts</span><span class="follow">Follow</span></div>
        <div class="tweet"><span class="avatar" role="img" aria-label="Profile picture"></span><div><span class="name">Critter Cover Surveys</span><br><span class="handle">@CritterSurveys</span><br>Lost on Saturday: Two cocker spaniel sisters from the village. Please share. Let's find these dogs</div><span class="date">21 Oct</span></div>
        <div class="tweet"><span class="avatar" role="img" aria-label="Profile picture"></span><div><span class="name">Critter Cover Surveys</span><br><span class="handle">@CritterSurveys</span></div><span class="date">21 Oct</span></div>
        <div class="tweetbox">Post to @CritterSurveys</div>
      </div>
    </div>

    <div class="ad">Advertisement<br>300 x 300</div>
  </section>

  <footer class="abs footer">
    <div class="counts">
      <div class="count"><span class="dot" style="background:var(--fb)" role="img" aria-label="Facepage"></span><span class="pill">35,000</span></div>
      <div class="count"><span class="dot" style="background:var(--tw)" role="img" aria-label="Chirper"></span><span class="pill">35,000</span></div>
      <div class="count"><span class="dot" style="background:#d8352a" role="img" aria-label="Clipstream"></span><span class="pill">35,000</span></div>
      <div class="count"><span class="dot" style="background:#c8202f" role="img" aria-label="Pinboardly"></span><span class="pill">35,000</span></div>
      <div class="count"><span class="dot" style="background:#3f729b" role="img" aria-label="Snapgram"></span><span class="pill">35,000</span></div>
    </div>
    <div class="foot-links"><span>About Us</span><span>Legal Information &amp; Disclaimers</span><span>Privacy Policy</span></div>
    <div class="copy">Copyright © 2015. Critter Cover Surveys UK.<br>All Right Reserved.</div>
  </footer>

</div>
</body>
</html>
```